Singapore Peer-to-Peer Business Loans Site Needs a Name Card Design

We need a name card design for a new company based in Singapore called 'Ledgerbloom Capital (Singapore) Pte. Ltd.' or in short, 'LedbolSG'.
We run an online platform where small and medium enterprises can access seed capital from wealthy persons seeking high yield returns.
We need a name card design - We would like to see designs that use the colours red, black and/or grey, using any combination of the logos that we have attached. The final design should communicate transparency, innovativeness, financial savvy, and professionalism.
Target Market(s)
Sophisticated/expert financial investors and small & medium business owners.
Industry/Entity Type
Financial

```html
<!DOCTYPE html>
<html lang="en">
<head>
<meta charset="utf-8">
<title>LedbolSG Name Card</title>
<link rel="stylesheet" href="https://fonts.googleapis.com/css2?family=Didact+Gothic&display=swap">
<style>
  :root {
    --paper: #ffffff;
    --ink: #1a1a1a;
    --ink-dark: #2e3033;
    --accent-red: #e42a2c;
    --card-grey: #9a9b9d;
    --frame-grey: #9a9a9a;
    --label-ink: #222222;
  }
  * { box-sizing: border-box; margin: 0; padding: 0; }
  html, body {
    width: 820px;
    height: 1200px;
    overflow: hidden;
    background: var(--paper);
    font-family: "Didact Gothic", "Century Gothic", sans-serif;
    color: var(--ink);
  }
  .sheet { position: relative; width: 820px; height: 1200px; }

  .side-label {
    position: absolute;
    left: 44px;
    font-size: 19px;
    letter-spacing: 0.5px;
    color: var(--label-ink);
  }
  .side-label--back { top: 64px; }
  .side-label--front { top: 660px; }

  .card {
    position: absolute;
    left: 40px;
    width: 780px;
    height: 446px;
  }
  .card--back {
    top: 98px;
    background: var(--paper);
    border: 1px solid var(--frame-grey);
  }
  .card--front {
    top: 698px;
    height: 460px;
    background: var(--card-grey);
  }

  .brand {
    position: absolute;
    left: 0;
    right: 0;
    display: flex;
    align-items: center;
    justify-content: center;
    gap: 16px;
  }
  .brand__mark {
    display: block;
    background: var(--accent-red);
  }
  .brand__name { line-height: 1; white-space: nowrap; }

  .card--back .brand { top: 70px; }
  .card--back .brand__mark { width: 44px; height: 44px; }
  .card--back .brand__name { font-size: 66px; color: var(--ink); }

  .card--front .brand { top: 178px; gap: 22px; }
  .card--front .brand__mark { width: 64px; height: 64px; }
  .card--front .brand__name { font-size: 100px; color: var(--ink-dark); }

  .holder {
    position: absolute;
    top: 196px;
    left: 0;
    right: 0;
    text-align: center;
  }
  .holder__name { font-size: 33px; line-height: 1; letter-spacing: 0.5px; color: var(--ink); }
  .holder__role { margin-top: 4px; font-size: 16px; color: var(--accent-red); }

  .contact {
    position: absolute;
    top: 338px;
    left: 0;
    right: 0;
    text-align: center;
    font-size: 19px;
    line-height: 28px;
    color: var(--ink);
  }
  .contact__line--links { font-size: 20px; }
  .contact__accent { color: var(--accent-red); }
  .contact__divider { color: var(--accent-red); margin: 0 8px; }
</style>
</head>
<body>
  <main class="sheet">
    <p class="side-label side-label--back">BACK</p>
    <section class="card card--back" aria-label="Card back">
      <div class="brand">
        <span class="brand__mark" aria-hidden="true"></span>
        <span class="brand__name">LedbolSG</span>
      </div>
      <div class="holder">
        <p class="holder__name">DANIEL TAN</p>
        <p class="holder__role">Financial Investor</p>
      </div>
      <div class="contact">
        <p class="contact__line">41 Harbour Lane, #18-00 Meridian Tower Centre, Singapore 049317</p>
        <p class="contact__line contact__line--links">Direct <span class="contact__accent">+</span> 65 6420 5173<span class="contact__divider">|</span>contact@ledbol.sg<span class="contact__divider">|</span>www.<span class="contact__accent">ledbol</span>.sg</p>
      </div>
    </section>

    <p class="side-label side-label--front">FRONT</p>
    <section class="card card--front" aria-label="Card front">
      <div class="brand">
        <span class="brand__mark" aria-hidden="true"></span>
        <span class="brand__name">LedbolSG</span>
      </div>
    </section>
  </main>
</body>
</html>
```